KettlesArmsPersonal

I am a cutting edge, top of the line gun store. We are expanding faster than we can keep up. We offer: Gunsmithing, Transfers, Concealed Carry, Machine Guns, Suppressors. My colors are reflected in my logo. Red, black and white. I like a clean design that gets the point across. I was trying to find a plastic business card, but will settle with a high quality paper product.

Industry/Entity Type

Plastic

Contact Information for Business Card

Dwayne Kettle - Owner
555-555-0148 (Cell)
Kettle's Arms Outfitters
4117 E. Hwy 9
Millbrook, NE 68999
sales@kettlesarmsoutfitters.example
kettlesarmsoutfitters.example

```html
<!DOCTYPE html>
<html lang="en">
<head>
<meta charset="utf-8">
<title>Kettle's Arms Outfitters – Business Card</title>
<link href="https://fonts.googleapis.com/css2?family=Open+Sans:wght@400;600;700&display=swap" rel="stylesheet">
<style>
  :root {
    --bg-top: #5c6575;
    --bg-bottom: #8a909c;
    --card-black: #2a2a2b;
    --card-black-dark: #1f1f20;
    --card-white: #ffffff;
    --brand-red: #b0242c;
    --ink-dark: #262626;
    --ink-light: #ffffff;
  }
  * { margin: 0; padding: 0; box-sizing: border-box; }
  html, body { width: 1200px; height: 1023px; overflow: hidden; }
  body {
    background: linear-gradient(180deg, var(--bg-top), var(--bg-bottom));
    font-family: "Open Sans", sans-serif;
    position: relative;
  }
  .card {
    position: absolute;
    left: 300px;
    width: 600px;
    height: 343px;
    border-radius: 22px;
    overflow: hidden;
    box-shadow: 0 10px 30px rgba(0,0,0,0.35);
  }
  .card--front {
    top: 138px;
    background: radial-gradient(ellipse at 50% 40%, #333334, var(--card-black-dark));
    color: var(--ink-light);
    display: flex;
    flex-direction: column;
    align-items: center;
    justify-content: center;
  }
  .brand { display: flex; align-items: center; gap: 14px; }
  .brand__mark { width: 26px; height: 26px; flex: none; }
  .card--front .brand__mark { background: var(--ink-light); }
  .brand__name { font-weight: 700; font-size: 34px; letter-spacing: 1px; white-space: nowrap; }
  .card--front .website { margin-top: 40px; font-size: 16px; letter-spacing: 0.3px; }
  .card--back { top: 541px; background: var(--card-white); }
  .back__band { position: absolute; inset: 0; width: 600px; height: 343px; }
  .card--back .brand { position: absolute; left: 40px; top: 52px; color: var(--ink-dark); }
  .card--back .brand__mark { background: var(--brand-red); }
  .card--back .brand__name { font-size: 28px; }
  .contact { position: absolute; left: 300px; top: 168px; color: var(--ink-light); }
  .contact__name { font-size: 21px; font-weight: 700; line-height: 1.1; }
  .contact__role { font-size: 14px; margin-bottom: 8px; }
  .contact__list { list-style: none; font-size: 12.5px; line-height: 1.55; }
  .contact__list li { display: flex; align-items: center; gap: 7px; white-space: nowrap; }
  .contact__list svg { width: 10px; height: 10px; flex: none; }
  .contact__address { font-size: 12.5px; line-height: 1.45; margin-top: 4px; }
</style>
</head>
<body>

<section class="card card--front" aria-label="Business card front">
  <div class="brand">
    <span class="brand__mark"></span>
    <span class="brand__name">Kettle's Arms Outfitters</span>
  </div>
  <p class="website">www.kettlesarmsoutfitters.example</p>
</section>

<section class="card card--back" aria-label="Business card back">
  <svg class="back__band" viewBox="0 0 600 343" preserveAspectRatio="none" aria-hidden="true">
    <path d="M0 170 Q300 120 600 100 L600 343 L0 343 Z" fill="var(--brand-red)"/>
    <path d="M0 178 Q300 128 600 108 L600 343 L0 343 Z" fill="var(--card-black)"/>
  </svg>

  <div class="brand">
    <span class="brand__mark"></span>
    <span class="brand__name">Kettle's Arms Outfitters</span>
  </div>

  <div class="contact">
    <p class="contact__name">Dwayne Kettle</p>
    <p class="contact__role">Owner</p>
    <ul class="contact__list">
      <li>
        <svg viewBox="0 0 10 10" aria-hidden="true"><rect x="2.5" y="0.5" width="5" height="9" rx="1" fill="none" stroke="#fff"/></svg>
        555-555-0148
      </li>
      <li>
        <svg viewBox="0 0 10 10" aria-hidden="true"><rect x="0.5" y="2" width="9" height="6" fill="none" stroke="#fff"/><path d="M0.5 2 L5 5.5 L9.5 2" fill="none" stroke="#fff"/></svg>
        sales@kettlesarmsoutfitters.example
      </li>
      <li>
        <svg viewBox="0 0 10 10" aria-hidden="true"><circle cx="5" cy="5" r="4.5" fill="#fff"/><path d="M0.5 5 H9.5 M5 0.5 V9.5" stroke="#2a2a2b" stroke-width="0.8"/></svg>
        www.kettlesarmsoutfitters.example
      </li>
    </ul>
    <p class="contact__address">Kettle's Arms Outfitters 4117 E.<br>Hwy 9 Millbrook, NE 68999</p>
  </div>
</section>

</body>
</html>
```